Electrical Business Card Design

New electrical business targeting my local area
Installations
Repairs
Switchboards
TV / Vistacast / Antennas
Telephone
Data Networks
Audio Visual
Licence # 518427K
ABN 58316927405
I would like some white background, black writing, red, blue & green can be used
Designer discretion to be used on layout, colour placement & any images
Reason: To give designers more time, I thought 5 days wasn't enough
Please don't just create generic business cards................include personal details e.g. business name, contact name, ph #, email. Also include the things I do, licence # & abn (refer to brief for all details)
Thanks
Reason: Would like more designs & have now committed my payment, thank you
Industry/Entity Type
Electrical
Contact Information for Business Card
Korvane Electrical Services,
Gareth Pelling,
0438 571 963,
korvaneelectrical@wexmail.net.au,
My suburb is Ryde
Look and feel

```html
<!DOCTYPE html>
<html lang="en">
<head>
<meta charset="utf-8">
<title>Korvane Electrical Services – Business Card</title>
<link rel="stylesheet" href="https://fonts.googleapis.com/css2?family=Jura:wght@600;700&family=Open+Sans:wght@400;700&display=swap">
<style>
  :root {
    --brand-blue: #3c3f97;
    --silver-dark: #c4c5c8;
    --silver-light: #f3f3f4;
    --page-bg: #ececec;
    --white: #ffffff;
  }
  * { box-sizing: border-box; margin: 0; padding: 0; }
  html, body {
    width: 1141px;
    height: 1200px;
    overflow: hidden;
    background: var(--page-bg);
  }
  .business-card {
    position: absolute;
    left: 70px;
    top: 314px;
    width: 1000px;
    height: 571px;
    overflow: hidden;
    background: linear-gradient(160deg, var(--silver-dark) 0%, var(--silver-light) 42%, var(--silver-light) 58%, var(--silver-dark) 100%);
    box-shadow: 0 6px 18px rgba(0,0,0,0.18);
  }
  .card-shapes {
    position: absolute;
    inset: 0;
    width: 1000px;
    height: 571px;
  }
  .card-shapes .fill-blue { fill: var(--brand-blue); }
  .company-name {
    position: absolute;
    left: 0;
    width: 1000px;
    top: 168px;
    text-align: center;
    font-family: "Jura", sans-serif;
    font-weight: 700;
    font-size: 50px;
    letter-spacing: 1px;
    color: var(--brand-blue);
  }
  .contact-person {
    position: absolute;
    left: 50px;
    top: 330px;
    font-family: "Open Sans", sans-serif;
    color: var(--white);
  }
  .contact-person .person-name {
    font-weight: 700;
    font-size: 29px;
    line-height: 1.1;
    text-transform: uppercase;
  }
  .contact-person .person-role {
    font-weight: 400;
    font-size: 22px;
    line-height: 1.2;
  }
  .contact-list {
    position: absolute;
    left: 478px;
    top: 306px;
    width: 500px;
    list-style: none;
    font-family: "Open Sans", sans-serif;
    font-size: 18px;
    color: var(--white);
  }
  .contact-list li {
    display: flex;
    align-items: center;
    height: 30px;
    white-space: nowrap;
  }
  .contact-list svg {
    width: 18px;
    height: 18px;
    margin-right: 12px;
    fill: var(--white);
    flex: none;
  }
</style>
</head>
<body>
  <main class="business-card">
    <svg class="card-shapes" viewBox="0 0 1000 571" aria-hidden="true">
      <rect class="fill-blue" x="60" y="38" width="320" height="14"/>
      <rect class="fill-blue" x="385" y="54" width="280" height="13"/>
      <rect class="fill-blue" x="120" y="56" width="250" height="5"/>
      <polygon class="fill-blue" points="0,290 412,290 396,462 0,462"/>
      <polygon class="fill-blue" points="426,290 439,290 423,472 410,472"/>
      <polygon class="fill-blue" points="454,290 1000,290 1000,482 437,482"/>
    </svg>

    <h1 class="company-name">Korvane Electrical Services</h1>

    <div class="contact-person">
      <p class="person-name">Gareth Pelling</p>
      <p class="person-role">Managing Director</p>
    </div>

    <ul class="contact-list">
      <li>
        <svg viewBox="0 0 24 24"><path d="M7 1h10a2 2 0 0 1 2 2v18a2 2 0 0 1-2 2H7a2 2 0 0 1-2-2V3a2 2 0 0 1 2-2zm0 3v14h10V4H7zm5 15.5a1.2 1.2 0 1 0 0 2.4 1.2 1.2 0 0 0 0-2.4z"/></svg>
        <span>0438 571 963</span>
      </li>
      <li>
        <svg viewBox="0 0 24 24"><path d="M9 16.2 4.8 12l-1.4 1.4L9 19 21 7l-1.4-1.4z"/></svg>
        <span>Installations · Repairs · Switchboards · Data · AV</span>
      </li>
      <li>
        <svg viewBox="0 0 24 24"><path d="M2 5h20v14H2V5zm2 2v.5l8 5 8-5V7H4zm0 2.8V17h16V9.8l-8 5-8-5z"/></svg>
        <span>korvaneelectrical@wexmail.net.au</span>
      </li>
      <li>
        <svg viewBox="0 0 24 24"><path d="M9 16.2 4.8 12l-1.4 1.4L9 19 21 7l-1.4-1.4z"/></svg>
        <span>Licence 518427K · ABN 58316927405</span>
      </li>
      <li>
        <svg viewBox="0 0 24 24"><path d="M12 2a7 7 0 0 0-7 7c0 5.2 7 13 7 13s7-7.8 7-13a7 7 0 0 0-7-7zm0 9.5a2.5 2.5 0 1 1 0-5 2.5 2.5 0 0 1 0 5z"/></svg>
        <span>Ryde NSW</span>
      </li>
    </ul>
  </main>
</body>
</html>
```